Website for SaaS CRM software

We require a cool website for a new SaaS CRM software. The design needs to be slick and modern. I quite like the look of sites like PostBadger.

The character 'Rhonda' in the video is the main character which we would like to incorporate on each page if possible. Like the chimp on Postbadger website.

'Sign Up Free' button or form to feature throughout the site so we have a strong call to action.

Here is a short video which will give you an idea of the software:
https://clipvault.example/83920417
Password: plintx

You can login to the user software (backend) for screen grabs and to see what the software is all about:
www.taskorbitq.example
Username: tenant8
Password: tenant8

Please note: The website is for the front end which is where we sell the software and NOT once the user has logged in.

Target Market(s)

Small businesses, freelancers, designers, 1-man businesses

Industry/Entity Type

Software

Requirements
Must have
• 1. Opt-in box for getting started for free:

'Sign up for your Free account'

2. Logos for social media : Qp/Chirpel/ViewDeck/JobLoop / K+
3. Friendora 'LIKE' button
4.The Navigation Bar should always be on display at the top when scrolling
5. Login button near the Navigation Bar
6. Login page or pop-up should also have 'Forgot Password' link which prompts them to enter their email so a password can be emailed to them.

5 pages & a blog in total. The pages we require are:

HOME
- Heading 'Easy to use small business software'
- Should have a video placeholder and some bullet points or tick marks for key features. The video (from ViewDeck) should open up on a bigger lightbox and the background greyed out.
- Sign up box to have the fields for First Name, Company Name, Email & Password with a check box for 'I agree with Terms & Conditions'

TOUR
Sub-Navigation bar at the top or side bar with the headings for each module i.e CONTACTS, QUOTES, JOBS, DIARY, SALES, PURCHASES, PRODUCTS, REPORTS
Each module with need to have a placeholder for an image or video and 1 paragraph of text explaining key features. Please see http://postbadger.example/features/

See how the Navigation buttons stay visible at all times and changes to the next button when scrolling: http://postbadger.example/features/

No side bar on this page.

PRICING
Pricing table of 3 to 4 columns with a button at the bottom. This software is a monthly subscription, so we need to show the $/month for each Plan at the top with the name of the Plan
The plans are:
Bronze: Free
Silver: $20/month
Gold: $40 / month
Platinum: $75 / month

No side bar on this page.

Heading at the bottom: 'No minimum contract. Cancel anytime.'

SUPPORT PAGE
This to a contact form to submit a ticket for tech support. We also need a 2-column list for videos which we will put up. The video open up on a lightbox in bigger size.

No side bar on this page.

CONTACT
Contact details i.e name, address, telephone, email & a contact form
No side bar on this page.

BLOG
Pagemill blog. I love the way the headings, paragraph, font, line spacing, colours are on the PostBadger blog.

Need a side bar.

```html
<!DOCTYPE html>
<html lang="en">
<head>
<meta charset="utf-8">
<title>Taskorbit – Easy to Use Small Business Software</title>
<link href="https://fonts.googleapis.com/css2?family=Ubuntu:ital,wght@0,400;0,500;0,700;1,400&display=swap" rel="stylesheet">
<style>
:root{
  --header-top:#ffffff;
  --header-bottom:#d9f6fb;
  --hero-light:#4fb8e6;
  --hero-mid:#2f9fd8;
  --hero-dark:#2a8ccb;
  --nav-bg:#1a5475;
  --nav-divider:#2d6c8f;
  --slider-btn:#1c4e6b;
  --ink:#111111;
  --white:#ffffff;
  --yellow:#fff200;
  --orange:#f7811d;
  --orange-dark:#e96a0c;
  --footer-bg:#222222;
  --footer-line:#3d3d3d;
  --footer-text:#b9b9b9;
  --footer-muted:#8c8c8c;
  --post-date:#f07d1b;
  --field-text:#777777;
}
*{margin:0;padding:0;box-sizing:border-box}
html,body{width:1200px;height:1020px;overflow:hidden}
body{font-family:"Ubuntu",sans-serif;position:relative;background:var(--footer-bg)}

/* header */
.site-header{position:absolute;left:0;top:0;width:1200px;height:125px;background:linear-gradient(var(--header-top),var(--header-bottom))}
.brand{position:absolute;left:130px;top:34px;font-size:50px;font-weight:700;color:var(--ink);letter-spacing:-1px;display:flex;align-items:center;gap:12px}
.brand-mark{width:26px;height:26px;border-radius:50%;background:var(--hero-mid)}
.login-link{position:absolute;left:1031px;top:27px;font-size:12px;font-weight:500;color:var(--ink);text-decoration:none}
.search{position:absolute;left:830px;top:57px;width:240px;height:30px;border:1px solid #c9d4d8;border-radius:3px;background:#fff}
.search span{position:absolute;left:11px;top:7px;font-size:12px;font-style:italic;color:#9a9a9a}
.search svg{position:absolute;right:8px;top:4px}

/* hero */
.hero{position:absolute;left:0;top:125px;width:1200px;height:558px;background:radial-gradient(ellipse at 45% 10%,var(--hero-light),var(--hero-mid) 55%,var(--hero-dark));overflow:hidden}
.bubble{position:absolute;border-radius:50%;background:rgba(255,255,255,.09)}
.main-nav{position:absolute;left:450px;top:20px;width:620px;height:51px;background:var(--nav-bg);border-radius:3px;display:flex}
.main-nav a{height:51px;line-height:51px;text-align:center;color:var(--white);font-size:15px;text-decoration:none;border-right:1px solid var(--nav-divider)}
.main-nav a:last-child{border-right:none}
.slide-btn{position:absolute;top:237px;width:62px;height:79px;background:var(--slider-btn);display:flex;align-items:center;justify-content:center}
.slide-photo{position:absolute;left:178px;top:100px;width:521px;height:360px;background:#fff;padding:6px;box-shadow:0 2px 6px rgba(0,0,0,.2)}
.slide-photo div{width:100%;height:100%;background:linear-gradient(135deg,#e4e7ea,#b8bcc0 45%,#454a55)}
.mascot{position:absolute;left:60px;top:285px;width:245px;height:270px;border-radius:40px 40px 20px 20px;background:linear-gradient(#f47a25,#f9b04a)}
.headline{position:absolute;left:723px;top:93px;color:var(--white);text-shadow:0 1px 2px rgba(0,0,0,.2)}
.headline h1{font-size:44px;font-weight:500;line-height:46px}
.headline h2{font-size:31px;font-weight:500;line-height:36px;letter-spacing:.3px}
.features{position:absolute;left:723px;top:181px;list-style:none}
.features li{height:36px;display:flex;align-items:center;gap:16px;color:var(--white);font-size:14px;font-weight:700}
.signup-title{position:absolute;left:723px;top:352px;color:var(--white);font-size:30px;font-weight:500}
.signup-title em{font-style:normal;color:var(--yellow)}
.field{position:absolute;width:167px;height:29px;background:#fff;border:1px solid #9fcde6;border-radius:4px;font-size:12px;color:var(--field-text);padding:7px 10px;letter-spacing:.3px}
.terms{position:absolute;left:723px;top:503px;display:flex;align-items:center;gap:9px;color:#0f2a3a;font-size:12px;font-weight:500}
.terms i{width:14px;height:14px;background:#f2f2f2;border:1px solid #8a8a8a;display:block}
.signup-btn{position:absolute;left:944px;top:489px;width:126px;height:40px;border-radius:3px;background:linear-gradient(var(--orange),var(--orange-dark));color:var(--white);font-size:16px;font-weight:700;text-align:center;line-height:40px;box-shadow:0 1px 3px rgba(0,0,0,.3)}

/* footer */
.site-footer{position:absolute;left:0;top:683px;width:1200px;height:337px;background:var(--footer-bg)}
.video-thumb{position:absolute;left:133px;top:13px;width:280px;height:242px;border-radius:8px 8px 14px 14px;background:linear-gradient(#e6e6e6,#bdbdbd)}
.video-thumb div{position:absolute;left:28px;top:12px;width:226px;height:146px;background:#5b5b5b}
.vline{position:absolute;top:22px;width:1px;height:228px;background:var(--footer-line)}
.col-title{position:absolute;top:18px;color:var(--white);font-size:22px;font-weight:500}
.post{position:absolute;left:451px;width:292px}
.post h4{color:var(--white);font-size:14px;font-weight:500;margin-bottom:1px}
.post p{color:var(--footer-text);font-size:12px;font-style:italic;line-height:23px}
.post small{display:block;color:var(--post-date);font-size:11px;font-style:italic;margin-top:1px}
.post-sep{position:absolute;left:451px;top:152px;width:292px;border-top:1px dashed #555}
.link-list{position:absolute;top:57px;list-style:none}
.link-list li{color:var(--footer-text);font-size:12px;height:30.7px}
.footer-rule{position:absolute;left:130px;top:272px;width:940px;height:1px;background:var(--footer-line)}
.copyright{position:absolute;left:130px;top:297px;font-size:11px;color:var(--footer-muted);letter-spacing:.3px}
.copyright b{color:var(--white);font-weight:400}
.follow{position:absolute;left:865px;top:296px;display:flex;align-items:center;gap:6px;color:var(--white);font-size:14px}
.follow span{margin-right:8px}
.follow i{display:block;width:16px;height:16px;border-radius:2px}
</style>
</head>
<body>

<header class="site-header">
  <div class="brand"><span>taskorbit</span><span class="brand-mark"></span></div>
  <a class="login-link" href="#">LOG IN</a>
  <div class="search">
    <span>Enter your Serach...</span>
    <svg width="28" height="22" viewBox="0 0 28 22"><circle cx="10" cy="9" r="7" fill="none" stroke="#1f7fc4" stroke-width="3"/><line x1="15" y1="14" x2="24" y2="20" stroke="#1f7fc4" stroke-width="4" stroke-linecap="round"/></svg>
  </div>
</header>

<section class="hero">
  <div class="bubble" style="left:300px;top:5px;width:125px;height:125px"></div>
  <div class="bubble" style="left:155px;top:45px;width:70px;height:70px"></div>
  <div class="bubble" style="left:225px;top:10px;width:45px;height:45px"></div>
  <div class="bubble" style="left:420px;top:40px;width:60px;height:60px"></div>

  <nav class="main-nav">
    <a href="#" style="width:95px">Home</a>
    <a href="#" style="width:97px">Tour</a>
    <a href="#" style="width:112px">Pricing</a>
    <a href="#" style="width:117px">Support</a>
    <a href="#" style="width:92px">Blog</a>
    <a href="#" style="width:107px">Contact</a>
  </nav>

  <div class="slide-btn" style="left:0"><svg width="16" height="26"><polyline points="13,2 3,13 13,24" fill="none" stroke="#fff" stroke-width="2"/></svg></div>
  <div class="slide-btn" style="left:1139px"><svg width="16" height="26"><polyline points="3,2 13,13 3,24" fill="none" stroke="#fff" stroke-width="2"/></svg></div>

  <figure class="slide-photo"><div role="img" aria-label="Photo of a business team meeting"></div></figure>
  <div class="mascot" role="img" aria-label="Brand mascot illustration"></div>

  <div class="headline">
    <h1>Easy to Use</h1>
    <h2>Small Business Software</h2>
  </div>

  <ul class="features">
    <li><svg width="18" height="16"><polyline points="2,8 7,13 16,2" fill="none" stroke="#fff200" stroke-width="3.5"/></svg>Lorem ipsum dolor sit amet.</li>
    <li><svg width="18" height="16"><polyline points="2,8 7,13 16,2" fill="none" stroke="#fff200" stroke-width="3.5"/></svg>Nam fermentum vestibulum purus id .</li>
    <li><svg width="18" height="16"><polyline points="2,8 7,13 16,2" fill="none" stroke="#fff200" stroke-width="3.5"/></svg>Morbi iaculis fringilla gravida.</li>
    <li><svg width="18" height="16"><polyline points="2,8 7,13 16,2" fill="none" stroke="#fff200" stroke-width="3.5"/></svg>Aliquam ullamcorper tempor.</li>
  </ul>

  <h3 class="signup-title">Sign Up its <em>FREE !</em></h3>
  <div class="field" style="left:723px;top:402px">First Name</div>
  <div class="field" style="left:904px;top:402px">Company Name</div>
  <div class="field" style="left:723px;top:441px">Email Address</div>
  <div class="field" style="left:904px;top:441px">Password</div>
  <label class="terms"><i></i>I agree with terms &amp; conditions</label>
  <div class="signup-btn">Sign Up Now</div>
</section>

<footer class="site-footer">
  <div class="video-thumb" role="img" aria-label="Laptop showing the product introduction video with a play button"><div></div></div>

  <div class="vline" style="left:427px"></div>
  <div class="vline" style="left:765px"></div>
  <div class="vline" style="left:928px"></div>

  <h3 class="col-title" style="left:450px">Recent Post</h3>
  <article class="post" style="top:55px">
    <h4>Fusce accumsan, elit a suscipit sagittis</h4>
    <p>Duis aliquam nibh a dui iaculis viverra id a velit.<br>Vivamus egestas risus in magna varius commodo....</p>
    <small>Posted on Dec20, 2012</small>
  </article>
  <div class="post-sep"></div>
  <article class="post" style="top:172px">
    <h4>Fusce accumsan, elit a suscipit sagittis</h4>
    <p>Duis aliquam nibh a dui iaculis viverra id a velit.<br>Vivamus egestas risus in magna varius commodo....</p>
    <small>Posted on Dec20, 2012</small>
  </article>

  <h3 class="col-title" style="left:786px">About Us</h3>
  <ul class="link-list" style="left:786px">
    <li>Aliquam molestie</li><li>Vivamus egestas risus</li><li>Aliquam molestie</li>
    <li>Vivamus egestas risus</li><li>Aliquam molestie</li><li>Vivamus egestas risus</li>
  </ul>

  <h3 class="col-title" style="left:946px">Contact Us</h3>
  <ul class="link-list" style="left:946px">
    <li>Aliquam molestie</li><li>Vivamus egestas risus</li><li>Aliquam molestie</li>
    <li>Vivamus egestas risus</li><li>Aliquam molestie</li><li>Vivamus egestas risus</li>
  </ul>

  <div class="footer-rule"></div>
  <p class="copyright">2012 <b>Taskorbit</b>. All Rights Reserved &nbsp;|&nbsp; Terms of Use &nbsp;|&nbsp; Privacy Policy</p>
  <div class="follow">
    <span>Follow Us on:</span>
    <i style="background:#3b5a9a"></i>
    <i style="background:#3aa3d6"></i>
    <i style="background:#2a78b5"></i>
    <i style="background:#f08a1c"></i>
    <i style="background:#c7251f"></i>
  </div>
</footer>

</body>
</html>
```